make a fireworks website

we are manufacturer of fireworks in Asia.
we need a HD fireworks website for showing product to all world customers.
we also need an register for member system,location, forum,products..etc
I added my Logo for the company.
brightnova.com.hk

and please message me if you have
any question.
here some example of website:
http://www.skyplumeshow.com/
http://www.tornelupyro.com/
http://www.quarvel-pyro.co.uk/
http://www.mirethpyro.co.uk/

```html
<!DOCTYPE html>
<html lang="en">
<head>
<meta charset="utf-8">
<title>BrightNova Fireworks</title>
<link href="https://fonts.googleapis.com/css2?family=Open+Sans:wght@400;600;700;800&family=Oswald:wght@500;700&display=swap" rel="stylesheet">
<style>
:root{
  --purple:#5b1f86;
  --purple-dark:#3e1060;
  --pink:#e3157a;
  --yellow:#f7c600;
  --ink:#222;
  --muted:#666;
  --dark:#16121b;
  --white:#fff;
  --line:#e2e2e2;
}
*{box-sizing:border-box;margin:0;padding:0}
html,body{width:706px;height:1200px;overflow:hidden}
body{font-family:"Open Sans",sans-serif;color:var(--ink);background:var(--white);font-size:9px}
.site{width:706px;height:1200px;position:relative}

/* header */
.header{height:50px;display:flex;align-items:center;justify-content:space-between;padding:0 60px;border-bottom:3px solid var(--purple)}
.brand{display:flex;align-items:center;gap:6px;font-weight:800;font-size:17px;color:var(--purple)}
.brand-dot{width:22px;height:22px;border-radius:50%;background:var(--pink)}
.header-right{display:flex;flex-direction:column;align-items:flex-end;gap:6px}
.utility{display:flex;gap:9px;align-items:center;font-size:7px;color:var(--muted)}
.cart{background:var(--yellow);color:var(--ink);font-weight:700;padding:2px 7px;border-radius:2px}
.search{width:64px;height:12px;border:1px solid var(--line);font-size:6px;color:#aaa;padding:1px 3px}
.nav{display:flex;gap:18px;font-weight:700;font-size:8px;text-transform:uppercase}
.nav .active{color:var(--pink);border-bottom:2px solid var(--pink)}

/* hero */
.hero{height:255px;position:relative;background:linear-gradient(90deg,#120c16 0%,#2a1a2e 45%,#6a3c52 75%,#2a1830 100%);overflow:hidden}
.hero-photo{position:absolute;right:0;top:0;width:60%;height:100%;background:radial-gradient(circle at 60% 40%,#f3c27a 0%,#b05a3a 25%,#3a1a2c 60%,transparent 80%)}
.hero-copy{position:absolute;left:60px;top:40px;width:250px;color:var(--white)}
.hero-kicker{font-family:"Oswald",sans-serif;color:var(--yellow);font-size:13px;letter-spacing:.5px}
.hero-title{font-family:"Oswald",sans-serif;color:var(--pink);font-size:44px;line-height:1;font-weight:700;margin:2px 0 8px}
.hero-text{font-size:7px;line-height:1.5;color:#ddd}
.btn-yellow{display:inline-block;background:var(--yellow);color:var(--ink);font-weight:800;font-size:8px;padding:5px 10px;margin-top:12px;text-transform:uppercase}
.dots{position:absolute;left:60px;bottom:20px;display:flex;gap:4px}
.dots i{width:7px;height:7px;border-radius:50%;background:#777;display:block}
.dots i:first-child{background:var(--white)}

/* browse */
.browse{height:248px;padding-top:24px;text-align:center}
.section-title{font-size:20px;font-weight:800;text-transform:uppercase}
.section-title span{color:var(--pink);text-transform:none}
.section-sub{font-size:7.5px;color:var(--muted);width:400px;margin:6px auto 16px;line-height:1.5}
.carousel{display:flex;align-items:center;justify-content:center;gap:6px}
.arrow{width:14px;height:22px;background:#ccc;color:var(--white);font-size:10px;line-height:22px}
.product{width:64px;font-size:6.5px;color:var(--muted)}
.product-img{height:82px;margin-bottom:5px;border-radius:2px}
.product.featured{border:2px solid var(--yellow);padding:3px;background:#fffbe8}
.g1{background:linear-gradient(#f1c82a,#c2402b)}
.g2{background:linear-gradient(#3a2a7a,#c23070)}
.g3{background:linear-gradient(#d83a2a,#f0b21e)}
.g4{background:linear-gradient(#2a6ab8,#e6c63a)}
.g5{background:linear-gradient(#c02a2a,#3a1a1a)}
.g6{background:linear-gradient(#e4e4e4,#b24aa0)}
.g7{background:linear-gradient(#1f3a6a,#d84e2a)}

/* dark band */
.band{height:225px;background:var(--dark);color:var(--white);display:flex;padding:24px 60px 0;gap:24px;position:relative}
.band-left{width:260px}
.band-title{font-size:17px;font-weight:800}
.band-title span{color:var(--pink)}
.new-item{display:flex;gap:12px;margin-top:10px}
.new-img{width:88px;height:110px;background:linear-gradient(#7a1a1a,#e2482a 60%,#f3b02a)}
.new-name{font-size:12px;font-weight:700;line-height:1.25}
.price{font-size:13px;font-weight:800;color:var(--yellow);margin-top:10px}
.avail{font-size:6.5px;color:#aaa}
.btn-pink{display:inline-block;background:var(--pink);color:var(--white);font-weight:700;font-size:7px;padding:4px 8px;margin-top:6px;text-transform:uppercase}
.band-right{flex:1}
.band-right h2{font-size:17px;font-weight:800;line-height:1.2}
.tabs{display:flex;gap:3px;margin:8px 0}
.tabs span{background:var(--yellow);color:var(--ink);font-size:6px;font-weight:700;padding:2px 5px}
.tabs span+span{background:#444;color:#ddd}
.band-right p{font-size:7px;line-height:1.6;color:#ccc}
.band .dots{bottom:14px}

/* sellers + testimonials */
.lower{height:285px;display:flex;padding:26px 60px 0;gap:30px}
.sellers{width:250px}
.lower h3{font-size:17px;font-weight:800;text-transform:uppercase;border-bottom:1px solid var(--line);padding-bottom:6px;margin-bottom:12px}
.lower h3 span{color:var(--pink);text-transform:none}
.seller-row{display:flex;gap:14px}
.seller{width:72px;text-align:center;font-size:6.5px;line-height:1.35}
.seller-img{height:82px;margin-bottom:5px}
.seller .price{color:var(--pink);font-size:10px;margin-top:3px}
.seller .btn-pink{font-size:6px;padding:3px 6px;margin-top:3px}
.testimonials{flex:1}
.quote{border:1px solid var(--line);padding:12px 14px;font-size:7px;line-height:1.6;color:var(--muted)}
.quote-sign{text-align:right;color:var(--pink);font-weight:700;margin-top:6px}
.quote-sign small{display:block;color:#999;font-weight:400}

/* footer */
.footer{height:120px;background:var(--purple);color:var(--white);display:flex;padding:16px 60px 0;gap:28px}
.footer h4{font-size:8px;font-weight:800;text-transform:uppercase;margin-bottom:6px}
.site-map{width:150px}
.links{display:grid;grid-template-columns:1fr 1fr;gap:2px 10px;font-size:6.5px;color:#e1d2ee}
.news{width:150px;font-size:6.5px;color:#e1d2ee}
.field{background:var(--white);height:14px;margin:6px 0;color:#999;padding:2px 4px;font-size:6px}
.news .btn-yellow{margin-top:0;font-size:6.5px;padding:3px 8px}
.location{flex:1;display:flex;gap:8px}
.map{width:100px;height:64px;background:linear-gradient(135deg,#d9d6c8,#b9c9a8)}
.address{font-size:6.5px;line-height:1.6;color:#e1d2ee;padding-top:14px}
.phone{display:flex;align-items:center;gap:4px;color:var(--white);font-weight:700}
.copyright{position:absolute;left:0;bottom:0;width:706px;height:12px;background:var(--purple-dark);color:#cbb6dc;font-size:6px;padding:2px 60px}
</style>
</head>
<body>
<div class="site">

<header class="header">
  <div class="brand"><span class="brand-dot"></span>BrightNova</div>
  <div class="header-right">
    <div class="utility">
      <span>Home</span><span>Videos</span><span>Gallery</span><span>Safety</span><span>Offers</span><span>Blog</span><span>Your Account</span>
      <span class="cart">Shopping Cart</span>
      <span class="search">Search</span>
    </div>
    <nav class="nav">
      <span class="active">Home</span><span>Products</span><span>Event Displays</span><span>Offers</span><span>Contact Us</span>
    </nav>
  </div>
</header>

<section class="hero">
  <div class="hero-photo" role="img" aria-label="Fireworks bursting over a city landmark at night"></div>
  <div class="hero-copy">
    <div class="hero-kicker">PERFECT FOR YOUR</div>
    <div class="hero-title">SPECIAL DAY</div>
    <p class="hero-text">Light up every celebration with vivid colour and sound. Our display range is built for weddings, birthdays and festivals, made with care and tested for safety in every batch we ship.</p>
    <span class="btn-yellow">Start Shopping</span>
  </div>
  <div class="dots"><i></i><i></i><i></i><i></i></div>
</section>

<section class="browse">
  <h2 class="section-title">Browse <span>Products</span></h2>
  <p class="section-sub">Light up your special event with our range of carefully selected fireworks, whether it's Bonfire Night, New Years, a Birthday or Anniversary, we have fireworks perfectly suited for creating your own display.</p>
  <div class="carousel">
    <span class="arrow">&#8249;</span>
    <div class="product"><div class="product-img g1" role="img" aria-label="Fountain fireworks"></div>Fountains</div>
    <div class="product"><div class="product-img g2" role="img" aria-label="Display kit boxes"></div>Display Kits</div>
    <div class="product featured"><div class="product-img g3" role="img" aria-label="Rocket fireworks"></div>Rockets</div>
    <div class="product"><div class="product-img g4" role="img" aria-label="Professional barrage cakes"></div>Pro Barrages</div>
    <div class="product"><div class="product-img g5" role="img" aria-label="Loud fireworks selection"></div>Loud Effects</div>
    <div class="product"><div class="product-img g6" role="img" aria-label="Wedding fireworks"></div>Wedding Fireworks</div>
    <div class="product"><div class="product-img g7" role="img" aria-label="Selection boxes"></div>Selection Boxes</div>
    <span class="arrow">&#8250;</span>
  </div>
</section>

<section class="band">
  <div class="band-left">
    <h2 class="band-title"><span>NEW</span> Fireworks</h2>
    <div class="new-item">
      <div class="new-img" role="img" aria-label="Red firework barrage box"></div>
      <div>
        <div class="new-name">Scarlet Comet Fireworks Barrage</div>
        <div class="avail">Availability: In stock</div>
        <div class="price">$14.99</div>
        <span class="btn-pink">Shop Now</span>
      </div>
    </div>
  </div>
  <div class="band-right">
    <h2>Professional Firework Displays &amp; Events</h2>
    <div class="tabs"><span>Weddings</span><span>Birthdays</span><span>Corporate</span><span>Festivals</span></div>
    <p>Our team designs full shows for any venue, from quiet gardens to open fields. Each display is planned with you, timed to music if you wish, and fired by trained crew who handle permits, setup and the clean up after the final shot.</p>
    <p style="margin-top:6px">Tell us your date, place and budget and we will send a tailored plan with effects, duration and safety details within two working days.</p>
  </div>
  <div class="dots"><i></i><i></i><i></i><i></i></div>
</section>

<section class="lower">
  <div class="sellers">
    <h3>Best <span>Sellers</span></h3>
    <div class="seller-row">
      <div class="seller"><div class="seller-img g2" role="img" aria-label="Spinner trio pack"></div>Twirling Petal Trio Pack<div class="price">$14.99</div><span class="btn-pink">Shop Now</span></div>
      <div class="seller"><div class="seller-img g1" role="img" aria-label="Barrage box"></div>Golden Gale Barrage<div class="price">$14.99</div><span class="btn-pink">Shop Now</span></div>
      <div class="seller"><div class="seller-img g4" role="img" aria-label="Spinning wheel firework"></div>Halo Spin Wheel<div class="price">$14.99</div><span class="btn-pink">Shop Now</span></div>
    </div>
  </div>
  <div class="testimonials">
    <h3>Latest <span>Testimonials</span></h3>
    <div class="quote">
      &ldquo;The show for our wedding was beyond anything we hoped for. The team arrived early, set everything up quietly and the finale had every guest cheering. Ordering was simple and the advice on choosing effects was clear and honest. We will book again next year.&rdquo;
      <div class="quote-sign">Mia R. Lowen<small>Hong Kong</small></div>
    </div>
  </div>
</section>

<footer class="footer">
  <div class="site-map">
    <h4>Site Map</h4>
    <div class="links">
      <span>Home</span><span>New Arrivals</span><span>Videos</span><span>Products</span><span>Gallery</span><span>Event Displays</span><span>Safety</span><span>Offers</span><span>Blog</span><span>Contact Us</span>
    </div>
  </div>
  <div class="news">
    <h4>Important Industry News</h4>
    Enter your email below to receive news and offers.
    <div class="field">Your email address</div>
    <span class="btn-yellow">Subscribe</span>
  </div>
  <div class="location">
    <div>
      <h4>Our Location</h4>
      <div class="map" role="img" aria-label="Street map of the warehouse area"></div>
    </div>
    <div class="address">
      88 Lantern Park Drive<br>Unit 4, Oakbrook<br>
      <div class="phone"><svg width="7" height="7" viewBox="0 0 10 10"><path d="M2 1l2 2-1 1.5c.7 1.4 1.6 2.3 3 3L7.5 6l2 2-1.5 1.5C4.5 9 1 5.5.5 2.5z" fill="#f7c600"/></svg>555-710-3386</div>
      <div class="phone"><svg width="7" height="7" viewBox="0 0 10 10"><path d="M2 1l2 2-1 1.5c.7 1.4 1.6 2.3 3 3L7.5 6l2 2-1.5 1.5C4.5 9 1 5.5.5 2.5z" fill="#f7c600"/></svg>555-710-9274</div>
    </div>
  </div>
</footer>
<div class="copyright">Copyright &copy; 2014 brightnova.com.hk | All rights reserved</div>

</div>
</body>
</html>
```